Chicago Property Management Flyer

We need a brochure/flyer to market our property management services to Chicago property owners. I believe that my preference is single page, double sided, but a bi-fold or tri-fold format may also work. I have provided our logo, and some example images in case that is helpful. Refer to our website at http://www.lumevarpm.net/ for more info.

Industry/Entity Type

Property Management

Font styles to use
Sans Serif

```html
<!DOCTYPE html>
<html lang="en">
<head>
<meta charset="utf-8">
<title>Lumevar Property Management – Tri-fold Brochure</title>
<link href="https://fonts.googleapis.com/css2?family=Open+Sans:wght@400;600&family=Roboto+Condensed:wght@400;700&display=swap" rel="stylesheet">
<style>
  :root {
    --navy: #0f3a63;
    --navy-deep: #0a2c4d;
    --navy-soft: #1d4f7e;
    --accent-green: #8dc63f;
    --text-light: #ffffff;
    --page-bg: #dfe2e6;
    --photo-dark: #3b3b3b;
    --photo-light: #c9c9c9;
  }
  * { box-sizing: border-box; margin: 0; padding: 0; }
  html, body { width: 1200px; height: 800px; overflow: hidden; }
  body {
    background: radial-gradient(ellipse at center, #f3f4f6 0%, var(--page-bg) 100%);
    font-family: "Open Sans", sans-serif;
    position: relative;
  }
  .brochure {
    position: absolute;
    left: 135px; top: 40px;
    width: 930px; height: 720px;
    display: grid;
    grid-template-columns: repeat(3, 1fr);
    background: linear-gradient(160deg, var(--navy-soft) 0%, var(--navy) 45%, var(--navy-deep) 100%);
    box-shadow: 0 18px 40px rgba(0,0,0,.25);
    overflow: hidden;
  }
  .city-backdrop {
    position: absolute; inset: 0;
    background:
      repeating-linear-gradient(90deg, rgba(255,255,255,.03) 0 18px, rgba(0,0,0,.05) 18px 34px),
      linear-gradient(180deg, rgba(255,255,255,.02), rgba(0,0,0,.1));
  }
  .panel {
    position: relative;
    display: flex;
    flex-direction: column;
    padding: 40px 28px 26px;
    color: var(--text-light);
    border-right: 1px solid rgba(0,0,0,.15);
  }
  .panel:last-child { border-right: none; }
  .feature { display: grid; grid-template-columns: 38px 1fr; gap: 10px; margin-bottom: 14px; }
  .feature-icon { width: 32px; height: 32px; margin-top: 16px; }
  .feature-title {
    font-family: "Roboto Condensed", sans-serif;
    font-weight: 700; font-size: 14px; color: var(--accent-green); margin-bottom: 2px;
  }
  .feature-text { font-size: 11px; line-height: 1.45; }
  .photo-circle {
    flex: none;
    width: 90px; height: 90px; border-radius: 50%;
    border: 3px solid var(--text-light);
    margin: 8px auto 0;
  }
  .photo-brick { background: radial-gradient(circle at 45% 40%, #b5533c, #7a3427 60%, #6d8a4c 100%); }
  .photo-stone { background: radial-gradient(circle at 50% 40%, #e2c98d, #b89a5c 60%, #7c8a5a 100%); }
  .brand {
    margin-top: auto;
    padding-top: 14px;
    text-align: center;
    font-family: "Roboto Condensed", sans-serif;
    font-weight: 700; font-size: 16px; line-height: 1.2; letter-spacing: .5px; color: var(--text-light);
  }
  .brand-mark { width: 22px; height: 22px; border: 2px solid var(--text-light); margin: 0 auto 8px; }
  .skyline-photo { position: absolute; left: 310px; top: 0; width: 620px; height: 720px; }
  .contact-list { list-style: none; position: relative; z-index: 2; }
  .contact-list li {
    display: flex; align-items: center; gap: 8px;
    font-family: "Roboto Condensed", sans-serif; font-weight: 700;
    font-size: 19px; margin-bottom: 8px;
  }
  .contact-list svg { width: 18px; height: 18px; flex: none; }
  .panel-middle { z-index: 1; }
</style>
</head>
<body>
<main class="brochure">
  <div class="city-backdrop" role="img" aria-label="Faded aerial photo of the Chicago skyline in blue tones"></div>

  <svg class="skyline-photo" viewBox="0 0 620 720" role="img" aria-label="Black and white aerial photo of downtown Chicago high-rises">
    <defs>
      <linearGradient id="skyGrey" x1="0" y1="0" x2="1" y2="1">
        <stop offset="0" stop-color="#c9c9c9"/>
        <stop offset=".5" stop-color="#8a8a8a"/>
        <stop offset="1" stop-color="#3b3b3b"/>
      </linearGradient>
    </defs>
    <path d="M130 720 Q330 330 620 170 L620 720 Z" fill="url(#skyGrey)"/>
  </svg>

  <section class="panel panel-left">
    <div class="feature">
      <svg class="feature-icon" viewBox="0 0 34 34"><polygon points="17,1 31,9 31,25 17,33 3,25 3,9" fill="var(--accent-green)"/><path d="M10 19h9l5-4-2-2-4 3h-8z" fill="#fff"/></svg>
      <div><h3 class="feature-title">Save Time and Headaches</h3>
      <p class="feature-text">We have a team in place to tackle all aspects of property management for you. Never worry about leasing, tenants, maintenance, regulations, etc.</p></div>
    </div>
    <div class="feature">
      <svg class="feature-icon" viewBox="0 0 34 34"><polygon points="17,1 31,9 31,25 17,33 3,25 3,9" fill="var(--accent-green)"/><path d="M9 17l8-7 8 7v8H9z" fill="none" stroke="#fff" stroke-width="2"/></svg>
      <div><h3 class="feature-title">Maximize Your Investment Assets</h3>
      <p class="feature-text">Your properties are expensive assets with lots of potential. Put the right professionals in place to protect, maintain, and maximize their value.</p></div>
    </div>
    <div class="feature">
      <svg class="feature-icon" viewBox="0 0 34 34"><polygon points="17,1 31,9 31,25 17,33 3,25 3,9" fill="var(--accent-green)"/><rect x="9" y="12" width="16" height="10" rx="1" fill="none" stroke="#fff" stroke-width="2"/><circle cx="17" cy="17" r="2.5" fill="#fff"/></svg>
      <div><h3 class="feature-title">Increase Income</h3>
      <p class="feature-text">With our experience and market knowledge we can establish optimal rent prices, lease apartments quickly, reduce turnover, and navigate complex housing agency processes to ensure maximum income to you.</p></div>
    </div>
    <div class="feature">
      <svg class="feature-icon" viewBox="0 0 34 34"><polygon points="17,1 31,9 31,25 17,33 3,25 3,9" fill="var(--accent-green)"/><circle cx="17" cy="17" r="6" fill="none" stroke="#fff" stroke-width="2"/><path d="M17 13v8M15 15h4" stroke="#fff" stroke-width="1.6"/></svg>
      <div><h3 class="feature-title">Reduce Expenses, Maximize Profits</h3>
      <p class="feature-text">Maximize your profits by benefitting from our economies of scale, systems and processes, specialized knowledge, industry network, and buying power.</p></div>
    </div>
    <div class="photo-circle photo-brick" role="img" aria-label="Photo of a red brick Chicago apartment building"></div>
    <div class="brand">
      <div class="brand-mark"></div>
      LUMEVAR PROPERTY<br>MANAGEMENT
    </div>
  </section>

  <section class="panel panel-middle">
    <div class="feature">
      <svg class="feature-icon" viewBox="0 0 34 34"><polygon points="17,1 31,9 31,25 17,33 3,25 3,9" fill="var(--accent-green)"/><circle cx="17" cy="17" r="7" fill="none" stroke="#fff" stroke-width="2"/><path d="M17 12v5l3 3" stroke="#fff" stroke-width="2" fill="none"/></svg>
      <div><h3 class="feature-title">Stay Informed</h3>
      <p class="feature-text">With access to all of your property information, documentation, and financials through your online portal of our property management system you and your accountant can stay informed as needed.</p></div>
    </div>
    <div class="feature">
      <svg class="feature-icon" viewBox="0 0 34 34"><polygon points="17,1 31,9 31,25 17,33 3,25 3,9" fill="var(--accent-green)"/><path d="M10 23V17M15 23V14M20 23V11M25 23V9" stroke="#fff" stroke-width="3"/></svg>
      <div><h3 class="feature-title">Grow Your Investment Portfolio</h3>
      <p class="feature-text">With our management team focused on profitably managing your existing properties, we can then help you expand to future investments.</p></div>
    </div>
    <div class="photo-circle photo-stone" role="img" aria-label="Photo of a sandstone courtyard apartment building"></div>
  </section>

  <section class="panel panel-right">
    <ul class="contact-list">
      <li><svg viewBox="0 0 18 18"><circle cx="9" cy="9" r="8" fill="none" stroke="#fff" stroke-width="1.5"/><path d="M6 5l2 2-1 1.5 2.5 2.5L11 10l2 2-1.5 1.5C9 13 5 9 4.5 6.5z" fill="#fff"/></svg>773-555-0148</li>
      <li><svg viewBox="0 0 18 18"><circle cx="9" cy="9" r="8" fill="none" stroke="#fff" stroke-width="1.5"/><ellipse cx="9" cy="9" rx="3.5" ry="8" fill="none" stroke="#fff" stroke-width="1.2"/><path d="M1 9h16" stroke="#fff" stroke-width="1.2"/></svg>www.lumevarpm.net</li>
      <li><svg viewBox="0 0 18 18"><rect x="1.5" y="4" width="15" height="11" fill="none" stroke="#fff" stroke-width="1.5"/><path d="M1.5 4l7.5 6 7.5-6" fill="none" stroke="#fff" stroke-width="1.5"/></svg>mark@lumevarpm.net</li>
    </ul>
  </section>
</main>
</body>
</html>
```